International Freight Forwarder need a business card

We need a logo design for a freight forwarding company . We are active in Sea Transportation, Truck transportation, and Air Transportation, The design should be have normal dimensions of a card and should not have cuts and holes in its design (printed design is required - lamination accepted)

The said company is agent and sales representative of 2 other Shipping companies (whose logos, name, and website should also be mentioned on the card)

Industry/Entity Type

Logistics

Contact Information for Business Card

Address is "No.7, 2nd Sarv Baghestan-e-Nouri, Tehran, IR
Tel number is +98 21 66394512
Fax number is +98 21 66395830
E-Mail address is info@roshanbarsaz.com
Website is www.roshanbarsaz.com

Open Layer Logos attached as well

Colors
33a6d7
0292cd
0255a3
3276b5
85abd2
85cae6
cee9f5
d5e2ee
ffffff

Requirements
Must have
• Main logo of Roshan Barsaz
• Logo of TQM Shipping Line
• London, United Kingdom
• tqmline.com
• Logo of Calm Reef Shipping
• Dubai, United Arab Emirates
• crsuae.com
• We require OPEN layer file to be submitted to us upon project selection.
Should not have
• Weird Designs such as cuts to the shape or holes in design.

```html
<!DOCTYPE html>
<html lang="en">
<head>
<meta charset="utf-8">
<title>Roshan Barsaz – Business Card</title>
<link href="https://fonts.googleapis.com/css2?family=Roboto:wght@400;500;700&display=swap" rel="stylesheet">
<style>
  :root {
    --navy: #263a80;
    --brand-blue: #2a4a9a;
    --partner-navy: #24357f;
    --partner-sky: #33a6d7;
    --ink: #444a52;
    --white: #ffffff;
    --backdrop: #e9ecf0;
  }
  * { margin: 0; padding: 0; box-sizing: border-box; }
  html, body { width: 1200px; height: 1200px; overflow: hidden; }
  body {
    background: var(--backdrop);
    font-family: "Roboto", Arial, sans-serif;
    position: relative;
  }
  .card {
    position: absolute;
    left: 214px;
    width: 772px;
    height: 440px;
    border-radius: 18px;
    overflow: hidden;
  }
  .card--front { top: 150px; background: var(--navy); color: var(--white); }
  .card--back { top: 632px; background: var(--white); }

  /* front */
  .brand-mark {
    position: absolute;
    left: 126px; top: 126px;
    width: 154px; height: 154px;
    border: 3px solid var(--white);
    border-radius: 50%;
  }
  .brand-name {
    position: absolute;
    left: 73px; top: 286px;
    width: 260px;
    text-align: center;
    font-size: 17px;
    font-weight: 500;
    line-height: 21px;
  }
  .divider {
    position: absolute;
    left: 334px; top: 100px;
    width: 2px; height: 238px;
    background: var(--white);
  }
  .contact-block { position: absolute; left: 369px; top: 86px; }
  .person-name { font-size: 31px; font-weight: 500; line-height: 38px; }
  .person-role { font-size: 20px; line-height: 26px; }
  .address { margin-top: 26px; font-size: 18.5px; line-height: 26px; }
  .contact-list { margin-top: 18px; list-style: none; }
  .contact-list li {
    display: flex; align-items: center; gap: 7px;
    font-size: 19px; line-height: 27.5px;
  }
  .contact-list svg { width: 17px; height: 17px; flex: none; }

  /* back */
  .brand-mark--large {
    position: absolute;
    left: 67px; top: 80px;
    width: 210px; height: 210px;
    border: 4px solid var(--brand-blue);
    border-radius: 50%;
  }
  .brand-name--large {
    position: absolute;
    left: 42px; top: 312px;
    width: 260px;
    text-align: center;
    color: var(--brand-blue);
    font-size: 22px;
    font-weight: 700;
    line-height: 26px;
  }
  .partner { position: absolute; left: 420px; }
  .partner--reef { top: 44px; }
  .partner--tqm { top: 244px; }
  .partner-head { display: flex; align-items: center; gap: 18px; height: 96px; }
  .partner-dot { width: 92px; height: 92px; border-radius: 50%; flex: none; }
  .partner--reef .partner-dot { background: var(--partner-navy); }
  .partner--tqm .partner-dot { background: var(--partner-sky); }
  .partner-name { font-size: 21px; font-weight: 700; line-height: 25px; }
  .partner--reef .partner-name { color: var(--partner-navy); }
  .partner--tqm .partner-name { color: var(--partner-sky); }
  .partner-details {
    margin-top: 14px;
    color: var(--ink);
    font-size: 19.5px;
    line-height: 25px;
  }
</style>
</head>
<body>

<section class="card card--front">
  <div class="brand-mark"></div>
  <p class="brand-name">Roshan Barsaz<br>International<br>Transport.Co L.L.c</p>
  <div class="divider"></div>
  <div class="contact-block">
    <h1 class="person-name">Daniel Hartley</h1>
    <p class="person-role">President &amp; CEO</p>
    <p class="address">No.7, 2nd Sarv<br>Baghestan-e-Nouri, Tehran, IR</p>
    <ul class="contact-list">
      <li>
        <svg viewBox="0 0 24 24" fill="none" stroke="currentColor" stroke-width="1.8"><path d="M5 3h4l2 5-2.5 1.5a11 11 0 0 0 6 6L16 13l5 2v4a2 2 0 0 1-2 2A16 16 0 0 1 3 5a2 2 0 0 1 2-2z"/></svg>
        +98 21 66394512
      </li>
      <li>
        <svg viewBox="0 0 24 24" fill="currentColor"><rect x="6" y="2" width="12" height="6"/><rect x="2" y="9" width="20" height="9" rx="2"/><rect x="6" y="15" width="12" height="7" fill="var(--white)" stroke="var(--navy)" stroke-width="1.5"/></svg>
        +98 21 66395830
      </li>
      <li>
        <svg viewBox="0 0 24 24" fill="none" stroke="currentColor" stroke-width="1.8"><rect x="2" y="5" width="20" height="14"/><path d="M2 5l10 8 10-8"/></svg>
        info@roshanbarsaz.com
      </li>
      <li>
        <svg viewBox="0 0 24 24" fill="none" stroke="currentColor" stroke-width="1.8"><circle cx="12" cy="12" r="10"/><ellipse cx="12" cy="12" rx="4.5" ry="10"/><path d="M2 12h20M4 7h16M4 17h16"/></svg>
        www.roshanbarsaz.com
      </li>
    </ul>
  </div>
</section>

<section class="card card--back">
  <div class="brand-mark--large"></div>
  <p class="brand-name--large">Roshan Barsaz<br>International<br>Transport.Co L.L.c</p>

  <div class="partner partner--reef">
    <div class="partner-head">
      <div class="partner-dot"></div>
      <p class="partner-name">Calm Reef<br>Shipping LLC</p>
    </div>
    <p class="partner-details">Dubai, United Arab Emirates<br>www.crsuae.com</p>
  </div>

  <div class="partner partner--tqm">
    <div class="partner-head">
      <div class="partner-dot"></div>
      <p class="partner-name">TQM<br>Shipping Line Ltd</p>
    </div>
    <p class="partner-details">London, United Kingdom<br>www.tqmline.com</p>
  </div>
</section>

</body>
</html>
```